Hal's Remedies Business Card Design Project

I need a business card designed for my pharmacy Hal's Remedies. I would like just the logo on one side, maybe with black background and white lettering. The other side I would also like to include my logo which is attached. Also, please include my name and the following information:
Hal Norwick Owner/Pharm D.
Business address is 7163 N Birch Rd Sioux Falls, SD 57291.
Phone number is 605-318-6027 and fax # is 605-318-6031.
my email address is hal@halsremedies.example.
My website is www.halsremedies.example.
My business hours are Monday-Friday 8am-7 pm. Saturday 8am-12 pm. Sunday Closed.
I would like the design to include my logo colors, black, white, and neon green. Silver may be added as a highlight. Thanks.
Pharmacy
See above in product description

```html
<!DOCTYPE html>
<html lang="en">
<head>
<meta charset="utf-8">
<title>Hal's Remedies Business Cards</title>
<link href="https://fonts.googleapis.com/css2?family=Open+Sans:wght@400;600;700&display=swap" rel="stylesheet">
<style>
  :root {
    --charcoal: #333335;
    --red: #c9252d;
    --white: #ffffff;
    --paper: #f4f4f4;
    --ink: #555555;
    --backdrop: #ececec;
  }
  * { box-sizing: border-box; margin: 0; padding: 0; }
  html, body { width: 1200px; height: 973px; overflow: hidden; }
  body {
    background: var(--backdrop);
    font-family: 'Open Sans', Arial, sans-serif;
    position: relative;
  }
  .card {
    position: absolute;
    width: 525px;
    height: 300px;
    overflow: hidden;
    box-shadow: 0 6px 18px rgba(0,0,0,0.18);
  }
  /* Front card */
  .card-front { left: 70px; top: 150px; background: var(--red); }
  .card-front .top-band {
    position: absolute; left: 0; top: 0; width: 100%; height: 140px;
    background: var(--charcoal);
  }
  .card-front .brand {
    position: absolute; left: 150px; top: 98px;
    display: flex; align-items: center; gap: 10px;
  }
  .brand-dot {
    width: 18px; height: 18px; border-radius: 50%;
    background: var(--white);
  }
  .brand-name {
    color: var(--white); font-weight: 700; font-size: 22px; letter-spacing: -0.3px;
  }
  .card-front .person {
    position: absolute; left: 300px; top: 150px; color: var(--white); text-align: left;
  }
  .person-name { font-size: 17px; font-weight: 400; letter-spacing: 0.3px; }
  .person-title { font-size: 9px; font-weight: 400; letter-spacing: 0.4px; margin-top: 1px; }
  .card-front .hours {
    position: absolute; left: 14px; bottom: 14px;
    color: var(--white); font-size: 9.5px; letter-spacing: 0.3px;
  }
  /* Back card */
  .card-back { left: 610px; top: 520px; background: var(--paper); }
  .card-back svg.shapes { position: absolute; left: 0; top: 0; }
  .card-back .brand {
    position: absolute; left: 40px; top: 178px;
    display: flex; align-items: center; gap: 10px;
  }
  .card-back .brand .brand-name { font-size: 20px; }
  .card-back .dark-person {
    position: absolute; right: 22px; top: 40px; color: var(--white); text-align: right;
  }
  .card-back .dark-person .person-name { font-size: 16px; }
  .contact {
    position: absolute; right: 70px; top: 140px; text-align: right; color: var(--ink);
  }
  .contact-name { color: var(--red); font-size: 16px; letter-spacing: 0.3px; }
  .contact-line { font-size: 9.5px; line-height: 1.45; }
  .contact-phones { margin-top: 12px; }
  .contact-rule {
    height: 1px; width: 150px; margin: 6px 0 6px auto;
    background: linear-gradient(to left, var(--red), rgba(201,37,45,0));
  }
  .contact-icons {
    position: absolute; right: 28px; top: 180px;
    display: flex; flex-direction: column; gap: 6px;
  }
</style>
</head>
<body>

  <section class="card card-front">
    <div class="top-band"></div>
    <div class="brand">
      <span class="brand-dot"></span>
      <span class="brand-name">Hal's Remedies</span>
    </div>
    <div class="person">
      <p class="person-name">HAL NORWICK</p>
      <p class="person-title">OWNER/PHARM D</p>
    </div>
    <p class="hours">MONDAY-FRIDAY 8AM-7 PM, SATURDAY 8AM-12 PM</p>
  </section>

  <section class="card card-back">
    <svg class="shapes" width="525" height="300" viewBox="0 0 525 300">
      <polygon points="0,0 140,0 270,125 310,300 0,300" fill="var(--red)"/>
      <polygon points="150,0 525,0 525,125 282,125" fill="var(--charcoal)"/>
    </svg>
    <div class="brand">
      <span class="brand-dot"></span>
      <span class="brand-name">Hal's Remedies</span>
    </div>
    <div class="dark-person">
      <p class="person-name">HAL NORWICK</p>
      <p class="person-title">OWNER/PHARM D</p>
    </div>
    <div class="contact">
      <p class="contact-name">HAL NORWICK</p>
      <p class="contact-line">7163 N Birch Rd Sioux Falls, SD 57291</p>
      <div class="contact-phones">
        <p class="contact-line">605-318-6027</p>
        <p class="contact-line">605-318-6031</p>
      </div>
      <div class="contact-rule"></div>
      <p class="contact-line">hal@halsremedies.example</p>
      <p class="contact-line">www.halsremedies.example</p>
    </div>
    <div class="contact-icons">
      <svg width="26" height="24" viewBox="0 0 26 24" aria-label="Phone">
        <polygon points="7,1 19,1 25,12 19,23 7,23 1,12" fill="var(--red)"/>
        <path d="M8 14 q5 -6 10 0 v2 h-10 z" fill="var(--white)"/>
        <rect x="10" y="9" width="6" height="2" fill="var(--white)"/>
      </svg>
      <svg width="26" height="24" viewBox="0 0 26 24" aria-label="Fax">
        <polygon points="7,1 19,1 25,12 19,23 7,23 1,12" fill="var(--red)"/>
        <rect x="7.5" y="7" width="11" height="8" fill="none" stroke="var(--white)" stroke-width="1.5"/>
        <rect x="11" y="16" width="4" height="2" fill="var(--white)"/>
      </svg>
    </div>
  </section>

</body>
</html>
```